Start up in business consultancy needs a business card

We need the business card's layout (we have already the logo). Our business is concerned on consultancy services delivered to companies on the matter of sustainability. Business card should be enough essentials and professional style.

Side A with the following info:
logo + a space for the claim (still to identify) + website of the company

Side B with the following info:
Name of business card holder + title of the business card holder + address of the company + space for mobile number, phone number, fax number + e-mail of business card holder + graphic details around.

Target Market(s)

Business of any sector

Industry/Entity Type

Business Service

Contact Information for Business Card

Name of the company:
Pianoverde srl
Società Benefit

Address of the company:
Via Lucerna, 7
21047 - Saronno (VA)

Website:
www.pianoverde.it

Name of the BC' holder:
Luca Ferentino

Title:
Co-fondatore

Email:
luca@pianoverde.it

Mobile:
+39 348 915 2074
Phone:
+39 348 915 2074
Fax:
+39 348 915 2074

Font styles to use
Other font styles liked:
• new gothic

```html
<!DOCTYPE html>
<html lang="it">
<head>
<meta charset="utf-8">
<title>Pianoverde – Business Card</title>
<link rel="stylesheet" href="https://fonts.googleapis.com/css2?family=Questrial&family=Mulish:wght@800&family=Exo+2:wght@700&family=Roboto:wght@400&display=swap">
<style>
  :root {
    --backdrop: #a9a7a8;
    --card: #f7f7f7;
    --brand-blue: #1465a7;
    --ink: #333333;
    --ink-soft: #3f3f3f;
    --band-grey: #4b4e52;
    --ghost: #e6e6e6;
  }
  * { margin: 0; padding: 0; box-sizing: border-box; }
  html, body { width: 1200px; height: 1200px; overflow: hidden; background: var(--backdrop); }
  .canvas { position: relative; width: 1200px; height: 1200px; }
  .card { position: absolute; width: 712px; height: 418px; background: var(--card); overflow: hidden; }
  .card-front { left: 238px; top: 118px; }
  .card-back { left: 231px; top: 644px; }

  /* front */
  .ghost-ring { position: absolute; left: 398px; top: 30px; width: 360px; height: 360px; border: 9px solid var(--ghost); border-radius: 50%; }
  .brand-mark { position: absolute; left: 138px; top: 134px; width: 134px; height: 134px; border: 5px solid var(--brand-blue); border-radius: 50%; }
  .brand-name { position: absolute; left: 289px; top: 170px; font-family: "Questrial", sans-serif; font-size: 47px; color: var(--brand-blue); letter-spacing: 0.5px; }
  .front-web { position: absolute; left: 0; right: 0; top: 373px; display: flex; justify-content: center; align-items: center; gap: 18px; font-family: "Questrial", sans-serif; font-size: 20px; color: var(--ink-soft); letter-spacing: 0.6px; }
  .front-web .rule { width: 62px; height: 2px; background: var(--brand-blue); }

  /* back */
  .back-mark { position: absolute; left: 551px; top: 32px; width: 110px; height: 110px; border: 4px solid var(--brand-blue); border-radius: 50%; }
  .company { position: absolute; left: 29px; top: 112px; font-family: "Mulish", sans-serif; font-weight: 800; font-size: 24px; color: var(--brand-blue); }
  .holder-name { position: absolute; left: 29px; top: 196px; font-family: "Exo 2", sans-serif; font-weight: 700; font-size: 28px; color: var(--ink); }
  .holder-title { position: absolute; left: 29px; top: 234px; font-family: "Roboto", sans-serif; font-size: 15px; color: var(--ink); }
  .contacts { position: absolute; left: 29px; top: 280px; list-style: none; font-family: "Questrial", sans-serif; font-size: 17px; color: var(--ink-soft); }
  .contacts li { display: flex; align-items: center; height: 22px; }
  .contacts svg { width: 16px; height: 16px; margin-right: 13px; fill: var(--brand-blue); }
  .address { position: absolute; right: 32px; top: 287px; text-align: right; font-family: "Questrial", sans-serif; font-size: 17px; line-height: 24px; color: var(--ink-soft); }
  .band-grey { position: absolute; left: 0; bottom: 0; width: 470px; height: 25px; background: var(--band-grey); }
  .band-blue { position: absolute; right: 0; bottom: 0; width: 265px; height: 50px; background: var(--brand-blue); clip-path: polygon(29px 0, 100% 0, 100% 100%, 0 100%); }
  .band-blue span { position: absolute; right: 32px; top: 14px; font-family: "Questrial", sans-serif; font-size: 17px; color: #fff; letter-spacing: 0.4px; }
</style>
</head>
<body>
<div class="canvas">
  <section class="card card-front">
    <div class="ghost-ring"></div>
    <div class="brand-mark"></div>
    <div class="brand-name">pianoverde</div>
    <div class="front-web"><span class="rule"></span><span>www.pianoverde.it</span><span class="rule"></span></div>
  </section>

  <section class="card card-back">
    <div class="back-mark"></div>
    <div class="company">Pianoverde srl Società Benefit</div>
    <div class="holder-name">Luca Ferentino</div>
    <div class="holder-title">Co-fondatore</div>
    <ul class="contacts">
      <li><svg viewBox="0 0 16 16"><path d="M4 0h8a1 1 0 0 1 1 1v14a1 1 0 0 1-1 1H4a1 1 0 0 1-1-1V1a1 1 0 0 1 1-1zm1 2v10h6V2z"/></svg>+39 348 915 2074</li>
      <li><svg viewBox="0 0 16 16"><path d="M1 5c0-2 3-3 7-3s7 1 7 3v1h-4V5H5v1H1zM3 8l2-2h6l2 2v6H3zm5 1a2 2 0 1 0 0 4 2 2 0 0 0 0-4z"/></svg>+39 348 915 2074</li>
      <li><svg viewBox="0 0 16 16"><path d="M4 1h8v4H4zM1 6h14v6h-3v3H4v-3H1zm4 4v4h6v-4z"/></svg>+39 348 915 2074</li>
      <li><svg viewBox="0 0 16 16"><path d="M0 3h16v1L8 9 0 4zm0 3l8 5 8-5v7H0z"/></svg>luca@pianoverde.it</li>
    </ul>
    <div class="address">Via Lucerna, 7 21047<br>Saronno (VA)</div>
    <div class="band-grey"></div>
    <div class="band-blue"><span>www.pianoverde.it</span></div>
  </section>
</div>
</body>
</html>
```